ONE PAGE WEB DESIGN NEEDED for Finance Company

We need a web design (ONE PAGE DESIGN ONLY) for a new finance website called Brightwell Lending. Brightwell Lending helps customers get the right loan, whether its a home loan, investment loan, business loan etc.

You are required to come up with just the homepage design. Professionalism and quality is the key factors in the successful design.

Here are a few design questions to help you out:

-
What information should be used on the page?
Ive provided a document which outlines all the information needed to put on homepage (attached to the brief - called brightwell_page_info). Also see the Must Have section below on this brief.

-
What links should appear in the navigation/footer?:
The navigation should provide links to the following pages (NOTE: services link has subcategories):
1 Homepage
2 Services
- Home loans
- Investment loans
- Refinancing loans
- Business loans
3 About Us
4 FAQ
5 Contact Us

-
What colors should be used in the design?
Our company colors - Cyan: #2EADE3, Blue: #004B70, White. Feel free to submit designs with slight variations if you feel it improves the design.

-
What should the layout of the page be?
This is up to you to come up with - we are open to different layouts for the page design (as long as they capture the information effectively and making it easy to understand).

Target Market(s)

Potential Home owners, Families and Business Owners

Industry/Entity Type

Business

Requirements
Must have
• - Must contain our logo (attached as PNG and Illustrator file)
- Winning designer must supply a Photoshop file (PSD) that will allow us.
Nice to have
• - Should include photos/images of families, professional groups, tradespeople etc (you can use stock photos from PixQuarry and I will purchase them once you are selected as the winning design)
- Link to a loan calculator somewhere on front page with a button 'Find out how much you could borrow' (or maybe even try adding a loan calculator to the homepage if you think this would look good)
- Page should have a main headline "Finding the right loan for you" or "Brightwell Lending finds the right loan for our customers."
- Must include Accreditation logos somewhere on the homepage (will try and supply these soon)
Should not have
• - Poor quality designs will not be considered
- Do not use clipart

```html
<!DOCTYPE html>
<html lang="en">
<head>
<meta charset="utf-8">
<title>Brightwell Lending — Home</title>
<link href="https://fonts.googleapis.com/css2?family=Bebas+Neue&family=Yanone+Kaffeesatz:wght@300;400&family=Source+Sans+3:wght@400;600&display=swap" rel="stylesheet">
<style>
  :root {
    --cyan: #2eade3;
    --blue: #004b70;
    --white: #ffffff;
    --nav-top: #3a3a3a;
    --nav-bottom: #151515;
    --charcoal: #2d2d2d;
    --strip: #333333;
    --photo-light: #e6e4e1;
    --photo-warm: #cdb8a6;
    --photo-cool: #8fb2c4;
    --photo-dark: #2b3a44;
  }
  * { margin: 0; padding: 0; box-sizing: border-box; }
  html, body {
    width: 1200px; height: 1109px; overflow: hidden;
    background: var(--charcoal);
    font-family: "Source Sans 3", sans-serif;
  }
  .page {
    position: relative;
    width: 1100px; height: 1017px;
    transform: scale(1.090909);
    transform-origin: 0 0;
  }
  .band { position: absolute; left: 0; width: 1100px; }

  /* Header */
  .site-header { top: 0; height: 61px; background: var(--white); }
  .brand {
    position: absolute; left: 257px; top: 24px;
    display: flex; align-items: center; gap: 6px;
    font-family: "Source Sans 3", sans-serif; font-weight: 600;
    font-size: 15px; color: var(--blue); letter-spacing: -0.2px;
  }
  .brand-dot { width: 12px; height: 12px; border-radius: 50%; background: var(--cyan); }

  /* Navigation */
  .main-nav {
    top: 61px; height: 38px;
    background: linear-gradient(var(--nav-top), var(--nav-bottom));
  }
  .main-nav ul { list-style: none; position: absolute; left: 257px; top: 0; display: flex; height: 38px; }
  .main-nav li {
    position: relative;
    font-family: "Bebas Neue", sans-serif; font-size: 14px; letter-spacing: 0.2px;
    color: var(--white); line-height: 38px; padding: 0 13px;
    border-left: 1px solid #474747;
  }
  .main-nav li:first-child { padding-left: 0; border-left: none; }
  .main-nav li.is-current::after {
    content: ""; position: absolute; left: 6px; bottom: 0;
    border: 5px solid transparent; border-bottom-color: var(--cyan); border-top: none;
  }

  /* Hero */
  .hero { top: 99px; height: 168px; background: var(--cyan); }
  .hero-panel { position: absolute; left: 257px; top: 0; width: 545px; height: 168px; background: var(--white); overflow: hidden; }
  .hero-art {
    position: absolute; left: 118px; top: 0; width: 310px; height: 168px;
    background: radial-gradient(ellipse at 50% 55%, #b9b3ad 0%, #dcd9d6 45%, var(--white) 75%);
  }
  .hero-title {
    position: absolute; left: 12px; top: 17px; width: 200px;
    font-family: "Yanone Kaffeesatz", sans-serif; font-weight: 300;
    font-size: 19px; line-height: 21px; color: var(--cyan);
  }
  .hero-tagline {
    position: absolute; right: 9px; bottom: 10px;
    font-family: "Yanone Kaffeesatz", sans-serif; font-weight: 300;
    font-size: 19px; color: var(--cyan);
  }
  .divider { top: 267px; height: 8px; background: var(--strip); }

  /* Intro */
  .intro { top: 275px; height: 215px; background: var(--blue); }
  .photo { position: absolute; }
  .photo-family {
    left: 258px; top: 14px; width: 272px; height: 182px;
    background: linear-gradient(160deg, var(--photo-light) 0%, var(--photo-warm) 55%, #9d8878 100%);
  }
  .body-copy { color: var(--white); font-size: 9.5px; line-height: 16.2px; }
  .intro .body-copy { position: absolute; left: 541px; top: 39px; width: 265px; }

  /* Services */
  .services { top: 490px; height: 170px; background: var(--cyan); }
  .services-heading {
    position: absolute; left: 281px; top: 23px;
    font-family: "Bebas Neue", sans-serif; font-size: 14px; color: var(--white); letter-spacing: 0.2px;
  }
  .service { position: absolute; top: 62px; color: var(--white); }
  .service h3 {
    font-family: "Bebas Neue", sans-serif; font-weight: 400; font-size: 13px;
    line-height: 13px; margin: 0 0 5px 10px; letter-spacing: 0.2px;
  }
  .service ul { list-style: none; }
  .service li {
    position: relative; padding-left: 10px;
    font-size: 9.5px; line-height: 11px; margin-bottom: 5.5px;
  }
  .service li::before {
    content: ""; position: absolute; left: 0; top: 3px;
    width: 6px; height: 6px; border-radius: 50%; background: var(--white);
  }
  .service-home { left: 281px; }
  .service-investment { left: 397px; }
  .service-refinance { left: 534px; }
  .service-refinance li { width: 125px; }
  .service-business { left: 693px; top: 62px; }

  /* Lenders */
  .lenders { top: 660px; height: 228px; background: var(--blue); }
  .lenders .body-copy { position: absolute; left: 257px; top: 69px; width: 270px; }
  .photo-team {
    left: 528px; top: 21px; width: 273px; height: 182px;
    background: linear-gradient(180deg, #dbe8ee 0%, var(--photo-cool) 40%, var(--photo-dark) 65%, #9fb3bd 100%);
  }

  /* Footer */
  .site-footer { top: 888px; height: 129px; background: var(--charcoal); }
  .copyright {
    position: absolute; left: 0; right: 0; bottom: 4px; text-align: center;
    font-family: "Yanone Kaffeesatz", sans-serif; font-size: 10px; color: var(--white);
  }
</style>
</head>
<body>
<div class="page">

  <header class="band site-header">
    <div class="brand"><span class="brand-dot"></span>Brightwell Lending</div>
  </header>

  <nav class="band main-nav">
    <ul>
      <li class="is-current">Home</li>
      <li>Services</li>
      <li>About Us</li>
      <li>FAQ</li>
      <li>Contact Us</li>
    </ul>
  </nav>

  <section class="band hero">
    <div class="hero-panel">
      <div class="hero-art" role="img" aria-label="Architectural sketch of a house under construction with rolled-up blueprints"></div>
      <h1 class="hero-title">Brightwell Lending finds the right loan for our customers</h1>
      <p class="hero-tagline">Finding the right loan for you</p>
    </div>
  </section>

  <div class="band divider"></div>

  <section class="band intro">
    <div class="photo photo-family" role="img" aria-label="Smiling family of four playing together"></div>
    <p class="body-copy">
      At Brightwell Lending we work hard to find the right loan for our customers. We do that because we are backed by sound industry knowledge, professional experience and a great customer service approach. Brightwell Lending guarantees that we will always tailor the best solution for your individual lending needs.<br>
      We can do that because we have access to a wide variety of lending options from major banks to non-bank lenders and we are committed to finding the right lending product for you.
    </p>
  </section>

  <section class="band services">
    <h2 class="services-heading">We offer a unique approach to help you find the right:</h2>
    <div class="service service-home">
      <h3>Home Loan</h3>
      <ul><li>Home buyers</li><li>First home buyers</li><li>Over 20 lenders</li></ul>
    </div>
    <div class="service service-investment">
      <h3>Investment Loan</h3>
      <ul><li>Property investment loans</li><li>Interest only loans</li></ul>
    </div>
    <div class="service service-refinance">
      <h3>Refinancing</h3>
      <ul><li>Refinancing for the best rate</li><li>Upsizing or downsizing</li><li>Change from a variable to a fixed rate</li></ul>
    </div>
    <div class="service service-business">
      <h3>Business Loan<br>Business Finance</h3>
      <ul><li>Long term</li><li>Short term</li><li>Equipment and Leasing</li></ul>
    </div>
  </section>

  <section class="band lenders">
    <p class="body-copy">
      There are many different loan products in the marketplace.<br>
      Brightwell Lending has access to a wide panel of lenders which means we can access bank and non-bank lenders that meet the individual needs of our customers.<br>
      Contact Brightwell Lending today on: 1800 555 210 to find out more.
    </p>
    <div class="photo photo-team" role="img" aria-label="Silhouetted business team meeting in front of bright office windows"></div>
  </section>

  <footer class="band site-footer">
    <p class="copyright">Copyright © Brightwell Lending 2013 All Rights Reserved</p>
  </footer>

</div>
</body>
</html>
```